Tea Box Design as well as tea bag packaging

design box and tea bag wrap for new product launch. I have added some guidelines for the size. Please make this and elegant Earthy tones. This is a high end premium hemp tea and this should be reflected in the design. Please include Organic Black Hemp Tea and another run that says Organic Green Hemp Tea. Both should say omega-3 and omega-6 fatty acids

Target Market(s)

health and wellness

Industry/Entity Type

Health

Font styles to use
Decorative
Script

Requirements
Must have
• earthy tones. elegant and tasteful.
• title of Veloa Hemp Black Tea and Veloa Hemp Green Tea
Nice to have
• cup of tea
Should not have
• Pot leaf

```html
<!DOCTYPE html>
<html lang="en">
<head>
<meta charset="utf-8">
<title>Veloa Hemp Green Tea – Box and Tea Bag Sleeve</title>
<link rel="stylesheet" href="https://fonts.googleapis.com/css2?family=Cinzel:wght@400;600&family=Montserrat:wght@300;400;600&display=swap">
<style>
:root{
  --paper:#ffffff;
  --dieline:#e8198b;
  --pattern:#7c7a2c;
  --panel:#5b5a24;
  --panel-light:#77742f;
  --gold:#e0bd63;
  --cream:#f4efe2;
  --ink:#333333;
  --tea-dark:#7a2f0c;
  --tea-light:#e9c58c;
}
*{box-sizing:border-box;margin:0;padding:0}
html,body{width:1200px;height:702px;overflow:hidden;background:var(--paper)}
body{position:relative;font-family:"Montserrat",sans-serif;color:var(--ink)}
.dielines{position:absolute;left:0;top:0}
.sleeve-label{position:absolute;font-size:10.5px;line-height:12px;font-weight:300;color:#222;white-space:nowrap;letter-spacing:-.2px}
.tab{position:absolute;width:9px;height:18px;background:#222}
.panel{position:absolute;background:radial-gradient(ellipse at 50% 30%,var(--panel-light),var(--panel) 70%);overflow:hidden}
.pattern{position:absolute;background:var(--pattern)}
.brand{position:absolute;left:0;right:0;text-align:center;font-family:"Cinzel",serif;font-weight:600;color:var(--gold);white-space:nowrap}
.photo{position:absolute;background:radial-gradient(ellipse at 40% 55%,var(--tea-dark) 0%,#b85a1c 25%,var(--tea-light) 55%,#f1e2c2 80%)}
.arch{border-radius:50% 50% 0 0/40% 40% 0 0}
.claim{position:absolute;left:0;right:0;text-align:center;font-family:"Cinzel",serif;color:var(--cream);letter-spacing:.4px;white-space:nowrap}
.pill{position:absolute;left:50%;transform:translateX(-50%);background:var(--cream);color:#5b5a24;font-family:"Cinzel",serif;border-radius:10px;white-space:nowrap;text-align:center;letter-spacing:.5px;line-height:1.3}
.badge{position:absolute;border-radius:50%;background:#6f7d2a;border:1.5px solid var(--cream)}
.copy{position:absolute;color:var(--cream);font-size:5.6px;line-height:7px}
.net{position:absolute;color:var(--cream);font-size:6px;line-height:7px;text-align:right;white-space:nowrap}
.mandatories{position:absolute;background:#fff;color:#333;font-size:5.5px;display:flex;align-items:center;justify-content:center}
.recycle{position:absolute;color:#fff;font-family:Arial,sans-serif;font-weight:700;font-size:6.5px;text-align:center}
.lid{transform:rotate(180deg)}
</style>
</head>
<body>

<!-- tea bag sleeve front -->
<div class="sleeve-label" style="left:92px;top:108px;width:90px;text-align:right">TEA BAG SLEAVE<br>FRONT</div>
<div class="tab" style="left:190px;top:38px"></div>
<div class="tab" style="left:367px;top:38px"></div>
<div class="panel" style="left:199px;top:34px;width:168px;height:159px">
  <div class="brand" style="top:36px;font-size:20px">Veloa</div>
  <div class="claim" style="top:79px;font-size:5px">RICH SOURCE OF OMEGA3 &amp; OMEGA6</div>
  <div class="photo arch" role="img" aria-label="Photo of a glass cup of amber hemp green tea" style="left:10px;top:88px;width:148px;height:71px"></div>
  <div class="pill" style="top:147px;font-size:5.2px;padding:1px 5px">ORGANIC HEMP GREEN TEA</div>
</div>

<!-- tea bag sleeve back -->
<div class="sleeve-label" style="left:382px;top:108px;width:72px;text-align:right">TEA BAG SLEAVE<br>BACK</div>
<div class="tab" style="left:472px;top:38px"></div>
<div class="tab" style="left:649px;top:38px"></div>
<div class="panel" style="left:481px;top:38px;width:168px;height:159px">
  <div class="brand" style="top:52px;font-size:20px">Veloa</div>
  <div class="copy" style="left:20px;right:20px;top:109px;text-align:center;font-size:4.6px;line-height:6.5px">Whole leaf green tea blended with organic hemp, a natural source of omega-3 and omega-6 fatty acids.</div>
</div>

<!-- box: patterned body -->
<div class="pattern" role="img" aria-label="Olive leafy vine pattern" style="left:44px;top:297px;width:1078px;height:215px"></div>
<div class="pattern" role="img" aria-label="Olive leafy vine pattern" style="left:798px;top:80px;width:324px;height:217px"></div>

<!-- side panel 1 -->
<div class="panel" style="left:110px;top:314px;width:84px;height:184px">
  <div class="brand" style="top:34px;font-size:14px">Veloa</div>
  <div class="claim" style="top:86px;font-size:3.4px;letter-spacing:.2px">RICH SOURCE OF OMEGA3 &amp; OMEGA6</div>
  <div class="photo arch" role="img" aria-label="Photo of a glass cup of hemp green tea" style="left:5px;top:92px;width:74px;height:88px"></div>
  <div class="pill" style="top:173px;font-size:3.4px;padding:0 3px">ORGANIC HEMP GREEN TEA</div>
</div>

<!-- front panel -->
<div class="panel" style="left:326px;top:314px;width:191px;height:184px">
  <div class="brand" style="top:34px;font-size:24px">Veloa</div>
  <div class="claim" style="top:91px;font-size:5.5px">RICH SOURCE OF OMEGA3 &amp; OMEGA6</div>
  <div class="photo arch" role="img" aria-label="Photo of a glass cup of amber hemp green tea" style="left:12px;top:100px;width:167px;height:84px"></div>
  <div class="badge" style="left:162px;top:92px;width:19px;height:19px"></div>
  <div class="pill" style="top:172px;font-size:5.6px;padding:1px 6px">ORGANIC HEMP GREEN TEA</div>
</div>
<div class="net" style="left:270px;top:492px">50 TEA BAGS<br>250gms Net</div>

<!-- side panel 2 -->
<div class="panel" style="left:648px;top:314px;width:85px;height:184px">
  <div class="brand" style="top:34px;font-size:14px">Veloa</div>
  <div class="claim" style="top:86px;font-size:3.4px;letter-spacing:.2px">RICH SOURCE OF OMEGA3 &amp; OMEGA6</div>
  <div class="photo arch" role="img" aria-label="Photo of a glass cup of hemp green tea" style="left:5px;top:92px;width:75px;height:88px"></div>
  <div class="pill" style="top:173px;font-size:3.4px;padding:0 3px">ORGANIC HEMP GREEN TEA</div>
</div>

<!-- back panel -->
<div class="panel" style="left:814px;top:314px;width:297px;height:184px">
  <div class="brand" style="left:16px;right:auto;width:110px;top:42px;font-size:22px">Veloa</div>
  <div class="photo" role="img" aria-label="Photo of a glass cup of tea on a wooden table" style="left:145px;top:20px;width:144px;height:57px"></div>
  <div class="pill" style="left:217px;top:73px;font-size:3.6px;padding:0 4px">ORGANIC HEMP GREEN TEA</div>
  <div class="copy" style="left:14px;top:89px;width:124px">COPY RELEVANT TO THE PRODUCT &amp; BENEFITS: Our organic green tea is blended with hemp leaf and seed, gently dried to keep its smooth, grassy flavour and natural omega-3 and omega-6 fatty acids.</div>
  <div class="copy" style="left:160px;top:89px;width:132px">Steep one bag in freshly boiled water for three minutes. Enjoy plain or with honey. Store in a cool, dry place away from sunlight.</div>
  <div class="recycle" style="left:14px;top:143px;width:60px">100% Recyclable
    <svg width="16" height="14" viewBox="0 0 16 14" style="display:block;margin:2px auto" aria-hidden="true"><path d="M8 1 L13 10 L3 10 Z" fill="none" stroke="#fff" stroke-width="2"/></svg>
    BPA FREE</div>
  <div class="mandatories" style="left:93px;top:142px;width:198px;height:36px">PRICING AND OTHER MADATORIES WILL FEATURE HERE.</div>
</div>

<!-- lid panel (upside down) -->
<div class="panel lid" style="left:864px;top:90px;width:191px;height:191px">
  <div class="brand" style="top:22px;font-size:22px">Veloa</div>
  <div class="claim" style="top:78px;font-size:5px">RICH SOURCE OF OMEGA3 &amp; OMEGA6</div>
  <div class="photo arch" role="img" aria-label="Photo of a glass cup of amber hemp green tea" style="left:5px;top:86px;width:181px;height:105px"></div>
  <div class="badge" style="left:159px;top:85px;width:19px;height:19px"></div>
  <div class="pill" style="top:176px;font-size:5px;padding:1px 6px">ORGANIC HEMP GREEN TEA</div>
</div>
<div class="net lid" style="left:1060px;top:88px;color:#3b3a14">50 TEA BAGS<br>250gms Net</div>

<!-- dielines -->
<svg class="dielines" width="1200" height="702" viewBox="0 0 1200 702" fill="none" stroke="var(--dieline)" stroke-width="0.9" aria-hidden="true">
  <rect x="44" y="297" width="1078" height="215"/>
  <line x1="260" y1="297" x2="260" y2="512"/>
  <line x1="583" y1="297" x2="583" y2="512"/>
  <line x1="798" y1="297" x2="798" y2="512"/>
  <rect x="798" y="80" width="324" height="217"/>
  <path d="M798 80 L814 48 L1106 48 L1122 80"/>
  <path d="M44 297 L60 264 L244 264 L260 297"/>
  <path d="M583 297 L599 264 L782 264 L798 297"/>
  <path d="M1122 297 L1154 313 L1154 496 L1122 512"/>
  <path d="M44 512 L80 580 L70 600 L110 646 L195 646 L235 600 L225 580 L260 512"/>
  <path d="M583 512 L618 580 L608 600 L648 646 L733 646 L773 600 L763 580 L798 512"/>
  <path d="M260 512 L260 646 L583 646 L583 512"/>
  <path d="M798 512 L798 646 L1122 646 L1122 512"/>
  <path d="M345 537 L345 547 L396 555 L390 562"/>
  <path d="M498 537 L498 547 L447 555 L453 562"/>
  <path d="M884 537 L884 547 L935 555 L929 562"/>
  <path d="M1037 537 L1037 547 L986 555 L992 562"/>
  <g stroke="#555" stroke-width="0.8">
    <path d="M28 48 H40 M44 33 V45"/>
    <path d="M1172 48 H1160 M1156 33 V45"/>
    <path d="M28 648 H40 M44 652 V664"/>
    <path d="M1172 648 H1160 M1156 652 V664"/>
  </g>
</svg>

</body>
</html>
```